Construction Company

Design a clutter free business card, it can be double-sided utilizing the logo for BDN Ltd simple with all relevant contact information.

Please also a letterhead design to function for the purposes of invoicing, all mail requirements, with header to be distinctive while the footer ties page together and incorporates all necessary information.

For now, please use generic / dummy text and when a winner is selected, I will disclose the contact information.

Hi Designers! Please read the updated brief which includes the design of a business card and letterhead. Thank you!

```html
<!DOCTYPE html>
<html lang="en">
<head>
<meta charset="utf-8">
<title>BDN Ltd — Business Card</title>
<link rel="stylesheet" href="https://fonts.googleapis.com/css2?family=Playfair+Display:wght@400;700&family=Libre+Baskerville:wght@400;700&display=swap">
<style>
  :root {
    --stage: #000000;
    --card: #f3f3f5;
    --gold: #d4bb26;
    --blue: #1049a0;
    --navy: #23488a;
    --ink: #1d3a8f;
    --white: #ffffff;
  }
  * { margin: 0; padding: 0; box-sizing: border-box; }
  html, body {
    width: 1200px; height: 1200px; overflow: hidden;
    background: var(--stage);
  }
  .stage { position: relative; width: 1200px; height: 1200px; }
  .card {
    position: absolute; left: 348px; width: 504px; height: 290px;
    background: var(--card); overflow: hidden;
  }
  .card--front { top: 266px; }
  .card--back { top: 644px; height: 288px; }
  .card__shapes { position: absolute; inset: 0; width: 100%; height: 100%; }
  .brand {
    position: absolute; left: 0; width: 100%; text-align: center;
    font-family: "Playfair Display", serif; font-weight: 400;
    color: var(--ink); letter-spacing: 1px; line-height: 1;
  }
  .card--front .brand { top: 100px; font-size: 44px; }
  .card--back .brand { top: 114px; font-size: 36px; }
  .website {
    position: absolute; top: 250px; left: 0; width: 100%; text-align: center;
    font-family: "Libre Baskerville", serif; font-size: 12.5px; color: var(--white);
  }
  .holder {
    position: absolute; left: 56px; top: 197px; width: 126px; text-align: center;
    font-family: "Libre Baskerville", serif;
  }
  .holder__name { font-size: 15px; font-weight: 700; color: var(--ink); letter-spacing: .5px; }
  .holder__role { font-size: 8.5px; font-weight: 700; color: var(--gold); letter-spacing: 2.6px; margin-top: 1px; }
  .contacts { position: absolute; left: 240px; top: 171px; list-style: none; }
  .contacts__item {
    display: flex; align-items: center; height: 21.5px;
    font-family: "Libre Baskerville", serif; font-size: 10px; font-weight: 700; color: var(--ink);
  }
  .contacts__icon { width: 22px; height: 22px; margin-right: 9px; flex: none; }
</style>
</head>
<body>
<main class="stage">

  <section class="card card--front" aria-label="Business card front">
    <svg class="card__shapes" viewBox="0 0 504 290" aria-hidden="true">
      <polygon points="0,127 252,208 0,290" fill="var(--gold)"/>
      <polygon points="504,127 252,208 504,290" fill="var(--blue)"/>
      <polygon points="0,290 252,208 504,290" fill="var(--navy)"/>
    </svg>
    <div class="brand">BDN Ltd</div>
    <div class="website">www.yourwebsite.com</div>
  </section>

  <section class="card card--back" aria-label="Business card back">
    <svg class="card__shapes" viewBox="0 0 504 288" aria-hidden="true">
      <polygon points="0,0 252,81 0,162" fill="var(--blue)"/>
      <polygon points="504,0 252,81 504,162" fill="var(--gold)"/>
      <polygon points="0,0 504,0 252,81" fill="var(--navy)"/>
    </svg>
    <div class="brand">BDN Ltd</div>

    <div class="holder">
      <div class="holder__name">YOUR NAME</div>
      <div class="holder__role">DESIGNATION</div>
    </div>

    <ul class="contacts">
      <li class="contacts__item">
        <svg class="contacts__icon" viewBox="0 0 22 22" aria-hidden="true">
          <rect x="4" y="4" width="14" height="14" transform="rotate(45 11 11)" fill="var(--gold)"/>
          <rect x="8.5" y="6" width="5" height="10" rx="1" fill="var(--ink)"/>
          <rect x="9.5" y="7.5" width="3" height="6" fill="var(--gold)"/>
        </svg>
        (000) 000-0000
      </li>
      <li class="contacts__item">
        <svg class="contacts__icon" viewBox="0 0 22 22" aria-hidden="true">
          <rect x="4" y="4" width="14" height="14" transform="rotate(45 11 11)" fill="var(--gold)"/>
          <path d="M8 7 L10 7 L10.6 9.2 L9.6 10 Q10.6 12 12 12.4 L12.8 11.4 L15 12 L15 14 Q11 15 8.6 11.4 Q7.4 9 8 7 Z" fill="var(--ink)"/>
        </svg>
        (000) 000-0000, (000) 000-0000
      </li>
      <li class="contacts__item">
        <svg class="contacts__icon" viewBox="0 0 22 22" aria-hidden="true">
          <rect x="4" y="4" width="14" height="14" transform="rotate(45 11 11)" fill="var(--gold)"/>
          <rect x="8.5" y="6.5" width="5" height="3" fill="var(--ink)"/>
          <rect x="7.5" y="10" width="7" height="4" fill="var(--ink)"/>
          <rect x="8.5" y="13" width="5" height="2.5" fill="var(--ink)"/>
        </svg>
        (000) 000-0000
      </li>
      <li class="contacts__item">
        <svg class="contacts__icon" viewBox="0 0 22 22" aria-hidden="true">
          <rect x="4" y="4" width="14" height="14" transform="rotate(45 11 11)" fill="var(--gold)"/>
          <rect x="7" y="8" width="8" height="6" fill="var(--ink)"/>
          <path d="M7 8 L11 11.5 L15 8" fill="none" stroke="var(--gold)" stroke-width="0.8"/>
        </svg>
        etc@youremail.com
      </li>
    </ul>
  </section>

</main>
</body>
</html>
```